NURSING: RISING PAST THE SHADOWED SILL

Size of the book cover: 140 x 215 mms

I need a cover for the 30,000 word book I have just written. It is a positive take on what I think nursing is and what it needs to be in the future. It is also my story of being nursed and of being a nurse.

My dream is that nurses honor themselves; that they look to the future with confidence and intelligence and that care continues to be delivered with compassionate person centeredness.

I define nursing as a professional workforce which, with probity, prevent or relieve distress; provide compassionate, safe, excellent care; and which contributes to the organization of healthcare.

The name comes from a Biblical parable Corlan 3:7-9. If a light is hidden under a bushel (basket) it is barely seen. If it is lit out from the basket it is clearly seen. As nurses we must continue to take up our mantel and ensure our light is seen and that it continues to shine the way we want it to.

As nurses we each take up our own lantern of caring, each in our own ways. To walk more brightly in our own paths of service.

The final design should show the specialness of nursing.

Target Market(s)

Nurses present, past and future

Industry/Entity Type

Healthcare

Font styles to use
Sans Serif
Other font styles liked:
• Whatever you think will suit

Colors
ec1f27
0393ce
9bcb3c

Requirements
Must have
• Be friendly, calming.
• NB: I am not sure whether the title should be in uppercase or not. Nursing could be uppercase and rising past the shadowed sill could be lower case. I leave it to you experienced people
Nice to have
• Something that depicts nursing...or is suggestive of nursing and the specialness of the work we do. How we bring our light to our patients as we 'hold them in the palms of out hands' and care for them. How they honor us by allowing us into their lives. Our rich past and out history allows us to be who we are today and we look to the future with confidence and hope
• I like rich colors, eg the color type you might find on a stained glass window in a church - rich emerald green or rich crimson red or the deep blue of a nurses cape
Should not have
• A dark cover
• clutter
• Religious overtone
• I have chosen three colors but they are not in the shading I would like - see above

```html
<!DOCTYPE html>
<html lang="en">
<head>
<meta charset="utf-8">
<title>Nursing: Rising Past the Shadowed Sill — Book Cover</title>
<link rel="stylesheet" href="https://fonts.googleapis.com/css2?family=Bebas+Neue&family=Cormorant+Garamond:ital,wght@0,500;0,600;1,500&family=Tinos&display=swap">
<style>
  :root {
    --page: #ffffff;
    --sky: #0893cf;
    --sky-glow: #1ec3f3;
    --band: #0a6f9c;
    --ink-light: #ffffff;
    --photo-light: #8edcf3;
    --photo-mid: #4fbde6;
  }
  * { margin: 0; padding: 0; box-sizing: border-box; }
  html, body { width: 1200px; height: 1000px; overflow: hidden; background: var(--page); }

  .cover {
    position: absolute; left: 12px; top: 102px; width: 1171px; height: 808px;
    background: radial-gradient(ellipse 420px 360px at 910px 700px, var(--sky-glow), var(--sky) 70%);
    color: var(--ink-light);
    overflow: hidden;
  }
  .band {
    position: absolute; left: 0; top: 293px; width: 100%; height: 260px;
    background: var(--band);
  }

  /* Back cover */
  .blurb {
    position: absolute; left: 56px; top: 33px; width: 455px;
    font-family: "Tinos", "Times New Roman", serif;
    font-size: 12.6px; line-height: 15.2px; text-align: justify;
  }
  .blurb p { margin-bottom: 15px; }
  .blurb p.gap { margin-top: 22px; }

  /* Spine */
  .spine {
    position: absolute; left: 550px; top: 327px;
    writing-mode: vertical-rl;
    font-family: "Bebas Neue", "Oswald", sans-serif;
    white-space: nowrap;
  }
  .spine-title { display: block; font-size: 66px; line-height: 48px; letter-spacing: 1px; }
  .spine-sub { display: block; font-size: 18.5px; line-height: 20px; letter-spacing: 0.2px; }

  /* Front cover */
  .author {
    position: absolute; left: 700px; top: 12px; width: 400px; text-align: center;
    font-family: "Cormorant Garamond", serif; font-weight: 600;
    font-variant: small-caps; font-size: 46px; letter-spacing: 1px; line-height: 1;
  }
  .foreword {
    position: absolute; left: 700px; top: 64px; width: 400px; text-align: center;
    font-family: "Cormorant Garamond", serif; font-weight: 600;
    font-variant: small-caps; font-size: 23px; letter-spacing: 0.5px;
  }
  .photo-portrait {
    position: absolute; left: 793px; top: 93px; width: 222px; height: 200px;
    background: radial-gradient(ellipse 120px 110px at 50% 60%, var(--photo-light), var(--photo-mid) 55%, rgba(8,147,207,0) 100%);
  }
  .photo-legs {
    position: absolute; left: 833px; top: 553px; width: 148px; height: 255px;
    background: radial-gradient(ellipse 80px 150px at 50% 45%, var(--photo-light), var(--photo-mid) 55%, rgba(8,147,207,0) 100%);
  }

  .quote {
    position: absolute; left: 650px; top: 312px; width: 480px; text-align: center;
    font-family: "Cormorant Garamond", serif; font-style: italic; font-weight: 500;
    font-size: 17.5px; line-height: 22px;
  }
  .title {
    position: absolute; left: 680px; top: 358px; width: 440px; text-align: center;
    font-family: "Bebas Neue", "Oswald", sans-serif;
    font-size: 152px; line-height: 140px; letter-spacing: 1px;
    text-shadow: 0 2px 4px rgba(0,0,0,0.25);
  }
  .subtitle {
    position: absolute; left: 680px; top: 500px; width: 440px; text-align: center;
    font-family: "Bebas Neue", "Oswald", sans-serif;
    font-size: 35px; line-height: 36px; letter-spacing: 0.5px;
  }
</style>
</head>
<body>
<main class="cover">
  <div class="band"></div>

  <section class="blurb" aria-label="Back cover text">
    <p>Nursing is seldom expressed the way that it is in this book. It is written by a person who has been nursed or nursing all her life and it is recounted with honesty and candour. Every reader will find something to take from this narrative and nurses will no doubt see something of their own life mirrored in the many anecdotes and stories.</p>
    <p>Nursing: Rising past the shadowed sill is a book which brings into the light the authors rich experience of the world and work of nursing. Through its words it subtly challenges individual nurses to think deeply about what ‘being a nurse’ means to them.</p>
    <p>What nurses do is a very big deal. Nurses choose to be nurses. No one tells them they have to do it but for some reason they decide to. The people they care for honour them by allowing them into their lives at what can be the most vulnerable and dramatic times of their life. How nurses position themselves, how they ‘walk’ with their patients, how they connect and care for them has consequences both for those in their care and for themselves.</p>
    <p class="gap">One of nursing’s unique realities is that the work crosses normal social boundaries. It is work that is not easily talked about outside of nursing, and the support nurses provide for each other is important in enabling them to remain healthy and able.</p>
    <p>Nursing has a rich history. Adelaide Verran lit her lantern of caring more than a century ago. The light from that lantern continues to glow and it is relit every moment of everyday by nurses all around the world as they go about their work.</p>
    <p>This book is more than just a story of nursing. It is the story and chronology of a professional life, intermingled with the telling of personal accounts and experiences. It also includes some special thoughts on nursing now and into the future. Nursing in the present day, presents many new challenges and opportunities. The workforce is one which adapts well to new ideas and situations.</p>
    <p class="gap">The future of nursing is in nurses hands and as such it can look to the future with confidence and pride.</p>
    <p>The writer salutes nurses everywhere.</p>
  </section>

  <div class="spine">
    <span class="spine-title">NURSING</span>
    <span class="spine-sub">RISING PAST THE SHADOWED SILL</span>
  </div>

  <h2 class="author">Maren Holloway</h2>
  <p class="foreword">Foreword by Tessa Carrow RN</p>

  <div class="photo-portrait" role="img" aria-label="Photo of a smiling nurse in light blue scrubs with a stethoscope, head and shoulders"></div>

  <p class="quote">“We each take up our own lantern of caring, each in our own ways,<br>to walk more brightly in our own path of service”</p>
  <h1 class="title">NURSING</h1>
  <p class="subtitle">RISING PAST THE SHADOWED SILL</p>

  <div class="photo-legs" role="img" aria-label="Photo of the nurse's lower body in light blue scrub trousers"></div>
</main>
</body>
</html>
```